Wordpress Template/Design for my business

I need a WordPress template to showcase my technical knowledge for my consultancy. Ideally it will use the same formatting your logo that you created for me.

bility to add tabs, and about me section which ill update

good examples:
http://www.brimwelltorque.com/
http://dellanpruitt.com/
http://joostvalkering.nl/

Target Market(s)

Technical people looking

Industry/Entity Type

Business

Number of Pages Required

3 page

Other font styles liked:
• See logo

Requirements
Must have
• A

```html
<!DOCTYPE html>
<html lang="en">
<head>
<meta charset="utf-8">
<title>Nimbara — Cloud Innovation</title>
<link rel="stylesheet" href="https://fonts.googleapis.com/css2?family=Lato:wght@400;700;900&family=Mulish:wght@300;400&display=swap">
<style>
  :root {
    --ink-dark: #232323;
    --ink-body: #3a3a3a;
    --brand-blue: #1a9fe0;
    --brand-blue-deep: #0d7fc8;
    --hero-navy: #0d1a33;
    --hero-mid: #1b3560;
    --page-bg: #ffffff;
    --card-border: #e3e3e3;
    --footer-bg: #3b3b3b;
    --white: #ffffff;
  }
  * { box-sizing: border-box; margin: 0; padding: 0; }
  html, body { width: 1095px; height: 1200px; overflow: hidden; }
  body { background: var(--page-bg); font-family: "Lato", sans-serif; color: var(--ink-body); position: relative; }

  .site-header { position: absolute; top: 0; left: 0; width: 1095px; height: 106px; background: var(--ink-dark); border-bottom: 1px solid #555; }
  .brand { position: absolute; left: 73px; top: 38px; display: flex; align-items: center; gap: 8px; }
  .brand-mark { width: 22px; height: 22px; border-radius: 50%; background: var(--brand-blue); }
  .brand-name { font-family: "Lato", sans-serif; font-weight: 700; font-size: 28px; color: var(--brand-blue); }
  .brand-tag { position: absolute; left: 103px; top: 72px; font-size: 11px; color: #ddd; }
  .contact-bar { position: absolute; right: 73px; top: 16px; display: flex; gap: 28px; }
  .contact-item { display: flex; align-items: center; gap: 7px; color: var(--white); font-size: 14px; font-weight: 700; }
  .contact-icon { width: 26px; height: 26px; border: 2px solid var(--brand-blue); border-radius: 50%; display: flex; align-items: center; justify-content: center; }
  .main-nav { position: absolute; right: 73px; top: 70px; display: flex; }
  .main-nav a { color: var(--white); text-decoration: none; font-size: 12.5px; font-weight: 700; padding: 0 26px; border-left: 1px solid #555; line-height: 24px; }
  .main-nav a:first-child { border-left: none; }
  .main-nav a:last-child { padding-right: 0; }

  .hero { position: absolute; top: 107px; left: 0; width: 1095px; height: 243px; background: radial-gradient(ellipse at 45% 35%, var(--hero-mid), var(--hero-navy) 75%); }
  .hero-caption { position: absolute; left: 0; bottom: 0; width: 100%; height: 57px; background: rgba(10,14,24,0.7); color: var(--white); font-weight: 700; font-size: 21px; text-align: center; line-height: 57px; }

  .sidebar-card { position: absolute; left: 73px; width: 268px; background: var(--white); border: 1px solid var(--card-border); box-shadow: 0 1px 5px rgba(0,0,0,0.1); }
  .profile-card { top: 367px; height: 470px; padding: 14px 14px; }
  .profile-title { display: flex; align-items: center; gap: 8px; font-size: 20px; font-weight: 900; color: var(--ink-dark); padding-bottom: 6px; border-bottom: 1px dotted #bbb; }
  .profile-title .accent { color: var(--brand-blue); }
  .profile-body { display: flex; gap: 10px; margin-top: 8px; }
  .profile-photo { width: 96px; height: 105px; background: linear-gradient(160deg, #8a6a52, #c79e80 55%, #6a5040); flex-shrink: 0; }
  .profile-text { font-size: 11.5px; line-height: 17px; letter-spacing: 0.9px; color: var(--ink-body); }
  .social-row { position: absolute; left: 14px; top: 168px; display: flex; gap: 7px; }
  .social-row span { width: 19px; height: 19px; border-radius: 3px; }
  .cta-call { position: absolute; left: 15px; top: 203px; width: 236px; height: 49px; background: linear-gradient(var(--brand-blue), var(--brand-blue-deep)); border-radius: 3px; display: flex; align-items: center; justify-content: center; gap: 12px; color: var(--white); font-weight: 700; font-size: 21px; }
  .video-frame { position: absolute; left: 15px; top: 269px; width: 236px; height: 178px; border: 1px solid #ccc; padding: 4px; }
  .video-still { width: 100%; height: 100%; background: linear-gradient(160deg, #6b5a48, #2d3440 60%, #1a2230); position: relative; }
  .video-play { position: absolute; left: 93px; top: 48px; width: 42px; height: 42px; border-radius: 50%; background: rgba(255,255,255,0.9); display: flex; align-items: center; justify-content: center; }
  .video-controls { position: absolute; left: 0; bottom: 0; width: 100%; height: 28px; background: rgba(0,0,0,0.85); display: flex; align-items: center; gap: 8px; padding: 0 8px; color: var(--white); font-size: 10px; font-weight: 700; }
  .video-track { flex: 1; height: 5px; background: #555; border-radius: 3px; position: relative; }
  .video-track::after { content: ""; position: absolute; left: 32px; top: -3px; width: 11px; height: 11px; border-radius: 50%; background: #999; }

  .promo-card { top: 862px; height: 256px; }
  .promo { position: absolute; width: 101px; height: 101px; }

  .articles { position: absolute; left: 379px; top: 391px; width: 642px; }
  .article { height: 255px; }
  .article-head { display: flex; gap: 20px; }
  .article-thumb { width: 159px; height: 105px; flex-shrink: 0; }
  .article-title { font-family: "Mulish", sans-serif; font-weight: 300; font-size: 25.5px; line-height: 35px; color: #111; margin-top: -3px; }
  .article-body { margin-top: 12px; font-size: 11.4px; line-height: 17px; letter-spacing: 0.15px; color: var(--ink-body); text-align: justify; }

  .site-footer { position: absolute; left: 0; bottom: 0; width: 1095px; height: 41px; background: var(--footer-bg); color: #eee; font-size: 12px; text-align: center; line-height: 41px; }
  .site-footer strong { font-weight: 900; }
</style>
</head>
<body>
  <header class="site-header">
    <div class="brand"><span class="brand-mark"></span><span class="brand-name">Nimbara</span></div>
    <div class="brand-tag">cloud innovation</div>
    <div class="contact-bar">
      <div class="contact-item">
        <span class="contact-icon"><svg width="12" height="9" viewBox="0 0 12 9"><rect x="0.5" y="0.5" width="11" height="8" fill="none" stroke="#1a9fe0"/><path d="M0.5 0.5 6 5 11.5 0.5" fill="none" stroke="#1a9fe0"/></svg></span>
        hello@nimbara-cloud.com
      </div>
      <div class="contact-item">
        <span class="contact-icon"><svg width="8" height="12" viewBox="0 0 8 12"><rect x="0.5" y="0.5" width="7" height="11" rx="1" fill="none" stroke="#1a9fe0"/><rect x="2" y="2" width="4" height="4" fill="#1a9fe0"/></svg></span>
        (012) 555 0147
      </div>
    </div>
    <nav class="main-nav">
      <a href="#">HOME</a><a href="#">ABOUT</a><a href="#">MY EXPERTISE</a><a href="#">CONTACT</a>
    </nav>
  </header>

  <section class="hero" role="img" aria-label="Dark blue banner of glowing hexagons holding technology icons">
    <div class="hero-caption">Lorem ipsum dolor sit amet, consectetur adipiscing elit</div>
  </section>

  <aside class="sidebar-card profile-card">
    <h2 class="profile-title">
      <svg width="18" height="18" viewBox="0 0 18 18"><circle cx="9" cy="5" r="4" fill="#333"/><path d="M1 18c0-5 3.5-7 8-7s8 2 8 7z" fill="#333"/></svg>
      <span><span class="accent">Mr. Evan</span> Marlowe</span>
    </h2>
    <div class="profile-body">
      <div class="profile-photo" role="img" aria-label="Portrait photo of the consultant"></div>
      <p class="profile-text">Lorem ipsum dolor sit amet, consectetur adipiscing elit. Sed vitae magna tellus. Aenean ante nunc, semper nec cursus non, rutrum ac eros. semper nec cursus non.</p>
    </div>
    <div class="social-row" aria-label="Social links">
      <span style="background:#3b5998"></span><span style="background:#1da1f2"></span><span style="background:#dd4b39"></span><span style="background:#0077b5"></span>
    </div>
    <div class="cta-call">
      <svg width="26" height="26" viewBox="0 0 24 24"><path d="M6.6 10.8c1.4 2.8 3.8 5.1 6.6 6.6l2.2-2.2c.3-.3.7-.4 1-.2 1.1.4 2.3.6 3.6.6.6 0 1 .4 1 1V20c0 .6-.4 1-1 1C10.6 21 3 13.4 3 4c0-.6.4-1 1-1h3.5c.6 0 1 .4 1 1 0 1.3.2 2.5.6 3.6.1.3 0 .7-.2 1z" fill="#fff"/></svg>
      CALL US TODAY
    </div>
    <div class="video-frame">
      <div class="video-still" role="img" aria-label="Video still of a team working at computers in an office">
        <div class="video-play"><svg width="14" height="16" viewBox="0 0 14 16"><path d="M0 0 14 8 0 16z" fill="#222"/></svg></div>
        <div class="video-controls">
          <svg width="10" height="11" viewBox="0 0 10 11"><path d="M0 0 10 5.5 0 11z" fill="#fff"/></svg>
          <span>04:59</span><span class="video-track"></span><span>10:35</span>
          <svg width="12" height="12" viewBox="0 0 12 12"><path d="M0 4h3l4-3v10L3 8H0z" fill="#fff"/><path d="M9 3a4 4 0 0 1 0 6" stroke="#fff" fill="none"/></svg>
        </div>
      </div>
    </div>
  </aside>

  <aside class="sidebar-card promo-card">
    <div class="promo" style="left:24px;top:21px;background:linear-gradient(#1d2a3a,#3a2424)" role="img" aria-label="Conference free passes promotional banner"></div>
    <div class="promo" style="left:142px;top:21px;background:linear-gradient(#2a8fe0,#1565c0)" role="img" aria-label="Storage appliance promotional banner"></div>
    <div class="promo" style="left:24px;top:133px;background:linear-gradient(#5a1f1f,#3a1414)" role="img" aria-label="Backup software promotional banner"></div>
    <div class="promo" style="left:142px;top:133px;background:linear-gradient(#2a3a5a,#121a2a)" role="img" aria-label="Software phone system promotional banner"></div>
  </aside>

  <main class="articles">
    <article class="article">
      <div class="article-head">
        <div class="article-thumb" style="background:linear-gradient(120deg,#05154a,#1f5fd0 55%,#0a1a55)" role="img" aria-label="Blue digital data streams"></div>
        <h3 class="article-title">Lorem ipsum dolor sit amet, consectetur adipiscing elit. Sed vitae magna tellus.</h3>
      </div>
      <p class="article-body">Lorem ipsum dolor sit amet, consectetur adipiscing elit. Sed vitae magna tellus. Aenean ante nunc, semper nec cursus non, rutrum ac eros. Vestibulum mattis justo ac dui bibendum consequat a ac ipsum. Praesent a arcu venenatis, auctor velit eu, suscipit libero. Quisque convallis, leo ac pharetra sagittis, ipsum arcu auctor urna, sit amet cursus risus augue in eros. Duis lacinia nisi vitae leo commodo, non finibus magna maximus. Sed posuere, neque eget bibendum pulvinar, ligula erat suscipit dolor, ut maximus arcu mi et tortor. Quisque imperdiet turpis et ligula mollis ultricies. Mauris lacinia rhoncus odio, at rutrum diam mollis eu.</p>
    </article>
    <article class="article">
      <div class="article-head">
        <div class="article-thumb" style="background:linear-gradient(150deg,#0b2440,#1d4f80 50%,#081828)" role="img" aria-label="Close-up of code on a blue screen"></div>
        <h3 class="article-title">Lorem ipsum dolor sit amet, consectetur adipiscing elit. Sed vitae magna tellus.</h3>
      </div>
      <p class="article-body">Lorem ipsum dolor sit amet, consectetur adipiscing elit. Sed vitae magna tellus. Aenean ante nunc, semper nec cursus non, rutrum ac eros. Vestibulum mattis justo ac dui bibendum consequat a ac ipsum. Praesent a arcu venenatis, auctor velit eu, suscipit libero. Quisque convallis, leo ac pharetra sagittis, ipsum arcu auctor urna, sit amet cursus risus augue in eros. Duis lacinia nisi vitae leo commodo, non finibus magna maximus. Sed posuere, neque eget bibendum pulvinar, ligula erat suscipit dolor, ut maximus arcu mi et tortor. Quisque imperdiet turpis et ligula mollis ultricies. Mauris lacinia rhoncus odio, at rutrum diam mollis eu.</p>
    </article>
    <article class="article">
      <div class="article-head">
        <div class="article-thumb" style="background:radial-gradient(circle at 35% 50%,#6fc8ff,#1a6fc0 40%,#062a5a)" role="img" aria-label="Glowing blue circuit board with a processor"></div>
        <h3 class="article-title">Lorem ipsum dolor sit amet, consectetur adipiscing elit. Sed vitae magna tellus.</h3>
      </div>
      <p class="article-body">Lorem ipsum dolor sit amet, consectetur adipiscing elit. Sed vitae magna tellus. Aenean ante nunc, semper nec cursus non, rutrum ac eros. Vestibulum mattis justo ac dui bibendum consequat a ac ipsum. Praesent a arcu venenatis, auctor velit eu, suscipit libero. Quisque convallis, leo ac pharetra sagittis, ipsum arcu auctor urna, sit amet cursus risus augue in eros. Duis lacinia nisi vitae leo commodo, non finibus magna maximus. Sed posuere, neque eget bibendum pulvinar, ligula erat suscipit dolor, ut maximus arcu mi et tortor. Quisque imperdiet turpis et ligula mollis ultricies. Mauris lacinia rhoncus odio, at rutrum diam mollis eu.</p>
    </article>
  </main>

  <footer class="site-footer">Copyright © 2016 <strong>NIMBARA</strong>. All Rights Reserved.</footer>
</body>
</html>
```